Halden High 20 year Reunion Memorial

I need a tasteful memorial poster with the names of those alumni that have deceased. The school colors are black, orange, silver and white. I would definately like the background to be black. At the top of the poster I would like it to read:
Halden Hight School Class of 1993.
This evening is dedicated in memory of
(followed by the names on the attached file

Industry/Entity Type

School

Requirements
Must have
• Black background

```html
<!DOCTYPE html>
<html lang="en">
<head>
<meta charset="utf-8">
<title>Halden High School Class of 1993 – Memorial Poster</title>
<link rel="stylesheet" href="https://fonts.googleapis.com/css2?family=PT+Sans&family=Cormorant+Garamond:ital,wght@1,500;1,600&display=swap">
<style>
  :root {
    --backdrop: #e6e6e6;
    --poster-black: #231f20;
    --silver-light: #fbfbfb;
    --silver-mid: #d9d9da;
    --silver-dark: #a9aaac;
    --title-ink: #231f20;
    --school-orange: #f7941d;
    --date-white: #ffffff;
  }
  * { margin: 0; padding: 0; box-sizing: border-box; }
  html, body {
    width: 1200px;
    height: 1200px;
    overflow: hidden;
    background: var(--backdrop);
  }
  .poster {
    position: absolute;
    left: 180px;
    top: 40px;
    width: 840px;
    height: 1120px;
    background: var(--poster-black);
    overflow: hidden;
  }
  .header-band {
    position: absolute;
    inset: 0 0 auto 0;
    width: 840px;
    height: 340px;
  }
  .school-name {
    position: absolute;
    top: 74px;
    width: 100%;
    text-align: center;
    font-family: "PT Sans", sans-serif;
    font-size: 84px;
    line-height: 1;
    color: var(--title-ink);
    letter-spacing: -0.5px;
  }
  .class-year {
    position: absolute;
    top: 166px;
    width: 100%;
    text-align: center;
    font-family: "PT Sans", sans-serif;
    font-size: 50px;
    line-height: 1;
    color: var(--title-ink);
  }
  .dedication {
    position: absolute;
    top: 350px;
    width: 100%;
    text-align: center;
    font-family: "Cormorant Garamond", serif;
    font-style: italic;
    font-weight: 600;
    font-size: 80px;
    line-height: 88px;
    color: var(--school-orange);
  }
  .memorial-list {
    position: absolute;
    top: 552px;
    left: 0;
    width: 100%;
    list-style: none;
  }
  .memorial-entry {
    display: flex;
    align-items: baseline;
    height: 71px;
  }
  .entry-name {
    width: 326px;
    text-align: right;
    font-family: "Cormorant Garamond", serif;
    font-style: italic;
    font-weight: 600;
    font-size: 46px;
    color: var(--school-orange);
  }
  .entry-dates {
    margin-left: 30px;
    font-family: "Cormorant Garamond", serif;
    font-style: italic;
    font-weight: 500;
    font-size: 29px;
    color: var(--date-white);
    white-space: nowrap;
  }
</style>
</head>
<body>
  <main class="poster">
    <svg class="header-band" viewBox="0 0 840 340" aria-hidden="true">
      <defs>
        <linearGradient id="silverRim" x1="0" y1="0" x2="0" y2="1">
          <stop offset="0" stop-color="#cfd0d2"/>
          <stop offset="1" stop-color="var(--silver-dark)"/>
        </linearGradient>
        <radialGradient id="silverFace" cx="0.5" cy="0.45" r="0.7">
          <stop offset="0" stop-color="var(--silver-light)"/>
          <stop offset="0.6" stop-color="#ececed"/>
          <stop offset="1" stop-color="var(--silver-mid)"/>
        </radialGradient>
      </defs>
      <path d="M0 0 H840 V172 Q420 476 0 172 Z" fill="url(#silverRim)"/>
      <path d="M0 0 H840 V150 Q420 450 0 150 Z" fill="url(#silverFace)"/>
    </svg>

    <h1 class="school-name">Halden High School</h1>
    <p class="class-year">Class of 1993</p>

    <h2 class="dedication">This evening is dedicated<br>in memory of</h2>

    <ul class="memorial-list">
      <li class="memorial-entry"><span class="entry-name">Clara Lindqvist</span><span class="entry-dates">May 7, 1975 - November 28, 1993</span></li>
      <li class="memorial-entry"><span class="entry-name">Mitchell Boyd</span><span class="entry-dates">April 22, 1975 - April 2, 2002</span></li>
      <li class="memorial-entry"><span class="entry-name">Tessa Nyland</span><span class="entry-dates">July 13, 1975 - October 5, 2011</span></li>
      <li class="memorial-entry"><span class="entry-name">Derek Lowell</span><span class="entry-dates">April 29, 1975 - June 10, 1997</span></li>
      <li class="memorial-entry"><span class="entry-name">Jonah Salazar</span><span class="entry-dates">August 28, 1975 - February 27, 2010</span></li>
      <li class="memorial-entry"><span class="entry-name">Melissa Sandoval</span><span class="entry-dates">January 26, 1975 - December 22, 2012</span></li>
      <li class="memorial-entry"><span class="entry-name">Corey Dalton</span><span class="entry-dates">April 29, 1975 - January 30, 2013</span></li>
    </ul>
  </main>
</body>
</html>
```